KAZ Freightworks #ALLKAZ Business Cards & Letterhead

I am looking to business cards designed for our organization. We are currently undergoing a small re-branding that is taking place. Our organization is called KAZ Freightworks and we are headquartered in Phoenix, AZ. We primarily provide transportation and logistics services to the Meridel Parcel Bureau who is our largest customer. I would like to see a design that incorporates name, title, contact info, website, and address (this will be different depending on the employee). I would also like to see some color on the business card using our logo colors or a variation. I would like our logo on the back of the business card with the website displayed. The final design should communicate that we are a next generation transportation operate that focuses on being driver-first, customer-centric, innovative, and sustainable.We would also like our #ALLKAZ catch phrase incorporated as well.
Updates

Decision maker traveling outside of the country until Monday, November 25th.

Target Market(s)

Transportation & Logistics

Industry/Entity Type

Trucking Company

Contact Information for Business Card

-First and Last Name
-Position Title
-Contact Phone
-Contact Email
-Physical Address

Font styles to use
Serif

Colors

Designer to choose colors to be used in the design.

Requirements
Must have
• -KAZ logo prominently displayed
• -#ALLKAZ catch phrase used
• -Some amount of color, design gradient, etc.
• -Logo on the back with website listed (https://www.kazfreightco.example)

```html
<!DOCTYPE html>
<html lang="en">
<head>
<meta charset="utf-8">
<title>KAZ Freightworks Business Card</title>
<link rel="stylesheet" href="https://fonts.googleapis.com/css2?family=Questrial&display=swap">
<style>
  :root {
    --page: #e8e5e0;
    --green: #3f8f22;
    --green-light: #6bb23a;
    --ink: #0d1a22;
    --white: #ffffff;
    --muted: #d9e0e4;
  }
  html, body {
    margin: 0;
    width: 1200px;
    height: 970px;
    overflow: hidden;
    background: var(--page);
    font-family: "Questrial", "Century Gothic", sans-serif;
  }
  .card {
    position: absolute;
    left: 80px;
    top: 190px;
    width: 1040px;
    height: 590px;
    border-radius: 26px;
    overflow: hidden;
    box-shadow: 0 18px 40px rgba(0,0,0,0.18);
  }
  .card-art {
    position: absolute;
    inset: 0;
    width: 1040px;
    height: 590px;
  }
  .card-text { position: absolute; color: var(--white); margin: 0; }
  .holder-name { left: 58px; top: 74px; font-size: 35px; letter-spacing: 0.5px; }
  .holder-title { left: 56px; top: 114px; font-size: 26px; color: var(--muted); }
  .holder-address { left: 58px; top: 168px; font-size: 23px; line-height: 31px; color: var(--muted); }
  .company-name { left: 54px; top: 396px; font-size: 32px; }
  .company-name .accent { color: var(--green-light); }
  .contact-list { position: absolute; left: 50px; top: 460px; margin: 0; padding: 0; list-style: none; }
  .contact-item {
    display: flex; align-items: center; gap: 12px;
    height: 34px; font-size: 24px; color: var(--muted);
  }
  .contact-icon { width: 26px; height: 26px; flex: none; }
  .brand-block {
    position: absolute;
    left: 520px; top: 60px;
    width: 480px; height: 480px;
    display: flex; flex-direction: column;
    align-items: center; justify-content: center;
  }
  .brand-name {
    display: flex; align-items: center; gap: 22px;
    margin: 0;
    font-size: 150px; line-height: 1; letter-spacing: 4px;
    color: var(--ink);
  }
  .brand-dot {
    width: 34px; height: 34px; border-radius: 50%;
    background: var(--green);
    flex: none;
  }
  .catchphrase {
    margin: 22px 0 0;
    font-size: 30px; letter-spacing: 3px;
    color: var(--green);
  }
</style>
</head>
<body>
  <main class="card">
    <svg class="card-art" viewBox="0 0 1040 590" aria-hidden="true">
      <defs>
        <linearGradient id="surface" x1="0" y1="0" x2="1" y2="1">
          <stop offset="0" stop-color="#f6f7f8"/>
          <stop offset="1" stop-color="#dde2e5"/>
        </linearGradient>
        <linearGradient id="greenBand" x1="0" y1="0" x2="1" y2="1">
          <stop offset="0" stop-color="#5fae2f"/>
          <stop offset="1" stop-color="#2f8a1a"/>
        </linearGradient>
        <linearGradient id="navyBand" x1="0" y1="0" x2="1" y2="1">
          <stop offset="0" stop-color="#142630"/>
          <stop offset="1" stop-color="#0b161d"/>
        </linearGradient>
      </defs>
      <rect class="surface" width="1040" height="590" fill="url(#surface)"/>
      <path class="navy-band" d="M0,270 C120,320 300,320 370,260 C430,200 470,60 560,0 H600 C510,60 445,190 445,300 C445,420 520,530 635,590 H0 Z" fill="url(#navyBand)"/>
      <path class="green-band" d="M0,0 H560 C470,60 430,200 370,260 C300,320 120,320 0,270 Z" fill="url(#greenBand)"/>
      <path class="swoosh-line" d="M0,278 C120,328 305,328 378,264 C440,205 480,62 572,0" fill="none" stroke="#f2f4f5" stroke-width="9"/>
    </svg>

    <p class="card-text holder-name">Dana Whitlock</p>
    <p class="card-text holder-title">Director</p>
    <p class="card-text holder-address">4170 North Cactus<br>Ridge Road<br>Glendale, AZ 85301</p>

    <p class="card-text company-name">KAZ <span class="accent">Freightworks</span></p>

    <ul class="contact-list">
      <li class="contact-item">
        <svg class="contact-icon" viewBox="0 0 26 26" aria-hidden="true"><circle cx="13" cy="13" r="11.5" fill="none" stroke="#4f9e2c" stroke-width="1.6"/><path d="M9,7 l2.5,0 1,3 -1.6,1.2 c0.8,1.8 1.8,2.8 3.4,3.6 l1.2,-1.6 3,1 0,2.5 c-5,0.6 -10,-4.4 -9.5,-9.7z" fill="#4f9e2c"/></svg>
        <span>602-555-0148</span>
      </li>
      <li class="contact-item">
        <svg class="contact-icon" viewBox="0 0 26 26" aria-hidden="true"><circle cx="13" cy="13" r="11.5" fill="none" stroke="#4f9e2c" stroke-width="1.6"/><rect x="7" y="9" width="12" height="8" fill="none" stroke="#4f9e2c" stroke-width="1.5"/><path d="M7,9 l6,5 6,-5" fill="none" stroke="#4f9e2c" stroke-width="1.5"/></svg>
        <span>info@kazfreightco.example</span>
      </li>
      <li class="contact-item">
        <svg class="contact-icon" viewBox="0 0 26 26" aria-hidden="true"><circle cx="13" cy="13" r="11.5" fill="none" stroke="#4f9e2c" stroke-width="1.6"/><circle cx="13" cy="13" r="6.5" fill="none" stroke="#4f9e2c" stroke-width="1.3"/><path d="M6.5,13 h13 M13,6.5 v13" stroke="#4f9e2c" stroke-width="1.2"/></svg>
        <span>www.kazfreightco.example</span>
      </li>
    </ul>

    <div class="brand-block">
      <p class="brand-name"><span class="brand-dot" aria-hidden="true"></span>KAZ</p>
      <p class="catchphrase">#ALLKAZ</p>
    </div>
  </main>
</body>
</html>
```